Bramblewick Affairs Web Design Project

This is a bit of a challenging request. Bramblewick Affairs (event planning) and ORB Gala Hireworks (event equipment rental), operate in the Northern Virginia area and we are in the process of marketing ourselves heavily as a "on stop celebration shop". Our customers range from large music festivals to smaller corporate functions. We are seeking to integrate two companies under one umbrella, our event planning company which also offers catering services " Bramblewick Affair, LLC" with our event rental equipment company "ORB Gala Hireworks." Both have new logos created through Pixel Harbor. I would like to have one portal that provides access to both companies and maintain the party rental URL as a stand alone to remain accessible to our loyal customers if possible. The only website that exist today is ORB Gala Hireworks with the URL (www.orbgalahub.example), which needs a complete redesign, as it is very antiquated. This URL should still be able to stand on its own as well as integrated/accessible into the new overall parent company BRamblewick Affairs/ Our goal is to is to communicate to our customers that we are energetic, modern company with fresh celebration ideas and the hardware to go with it. There are numerous photos that need to be uploaded to the rental part of site. We will need to be able to update and make changes to photos without outside support.

Reason: I am changing the project to being a non-refundable and hope to get more submissions.

Target Market(s)

A very broad range of customers, from large rock festivals, to small country weddings and corporate functions

Industry/Entity Type

Event Planning

Requirements
Must have
• Must Have:
- - Ability to add and update photos without external support
-Modern interface ( look and feel)
-Easy user centered design
- multiple sections ( tabs) such as , Home, Event Planning, Catering, Galleries, Venues, Contact Us
Nice to have
• - ability to place event rental orders online

```html
<!DOCTYPE html>
<html lang="en">
<head>
<meta charset="utf-8">
<title>ORB Gala Hireworks</title>
<link href="https://fonts.googleapis.com/css2?family=Roboto:wght@300;400;500;700&display=swap" rel="stylesheet">
<style>
:root{
  --purple:#5a3b98;
  --purple-dark:#4b2f86;
  --orange:#f2692a;
  --text-grey:#7a7a7a;
  --top-bar:#f1f1f1;
  --card:#f4f4f4;
  --footer:#eeeeee;
  --white:#ffffff;
  --dark:#222222;
}
*{box-sizing:border-box;margin:0;padding:0}
html,body{width:1064px;height:1200px;overflow:hidden}
body{position:relative;background:var(--white);font-family:"Roboto",Arial,sans-serif;color:var(--text-grey)}
.abs{position:absolute}

.top-bar{left:0;top:0;width:1064px;height:42px;background:var(--top-bar)}
.search{left:787px;top:9px;width:161px;height:25px;display:flex}
.search-field{flex:1;background:var(--white);font-size:8px;color:#666;padding-left:9px;line-height:25px;letter-spacing:.3px}
.search-btn{width:25px;height:25px;background:var(--purple);display:flex;align-items:center;justify-content:center}

.brand{left:109px;top:59px;height:66px;display:flex;align-items:center;gap:12px}
.brand-dot{width:64px;height:64px;border-radius:50%;background:var(--purple)}
.brand-name{font-size:24px;font-weight:700;color:var(--orange);letter-spacing:.5px}

.main-nav{left:442px;top:88px;display:flex;gap:0}
.main-nav a{font-size:17px;color:var(--purple);text-decoration:none;margin-right:22px}
.main-nav a:last-child{margin-right:0}

.hero{left:106px;top:141px;width:852px;height:356px;background:linear-gradient(120deg,#5b4d8f 0%,#8e6fc0 22%,#b8a7c8 45%,#7d6a9a 65%,#4e4270 100%)}
.order-panel{left:675px;top:174px;width:209px;height:285px;background:var(--white);border-radius:6px;padding:17px 18px}
.order-title{font-size:14px;color:var(--purple);margin-bottom:15px}
.order-field{height:28px;background:#f5f5f5;border:1px solid #eee;font-size:8px;color:#888;line-height:28px;padding-left:8px;margin-bottom:9px;position:relative}
.order-field.select::after{content:"";position:absolute;right:8px;top:11px;border-left:4px solid transparent;border-right:4px solid transparent;border-top:7px solid var(--dark)}
.order-btn{display:block;margin:15px auto 0;width:102px;height:29px;background:var(--orange);color:var(--white);font-size:13px;font-weight:500;text-align:center;line-height:29px}
.slide-arrow{width:25px;height:25px;border-radius:50%}
.slide-prev{left:892px;top:460px;background:#eeeeee}
.slide-next{left:923px;top:460px;background:var(--orange)}

.welcome-title{left:0;top:524px;width:1064px;text-align:center;font-size:17px;color:var(--purple)}
.welcome-text{left:112px;top:568px;width:840px;text-align:center;font-size:13px;font-weight:300;line-height:21.5px}

.card{top:678px;width:266px;height:361px;background:var(--card);border-radius:8px}
.card-how{left:115px}
.card-gallery{left:399px}
.card-events{left:683px}
.card-title{position:absolute;left:20px;top:22px;font-size:17px;color:var(--purple)}
.card-copy{position:absolute;font-size:13px;font-weight:300;line-height:21.3px;text-align:justify}

.video{left:20px;top:66px;width:226px;height:132px;background:linear-gradient(135deg,#7b7297,#a89cc0 40%,#d8d3de 70%,#8d86a0)}
.video-bar{position:absolute;left:0;bottom:0;width:100%;height:28px;background:#1d1d1d}
.play{position:absolute;left:93px;top:35px;width:38px;height:38px;border-radius:50%;background:#2c2c2c}

.gallery-main{left:20px;top:66px;width:226px;height:143px;background:linear-gradient(160deg,#6b4c94,#9c80b8 40%,#4e3a63 75%,#2f2638)}
.g-arrow{position:absolute;top:62px;width:24px;height:24px;border-radius:50%;background:#f2f2f2}
.thumb{width:73px;height:53px}

.partner{left:18px;top:20px;display:flex;align-items:center;gap:9px}
.partner-dot{width:26px;height:26px;border-radius:50%;background:var(--orange)}
.partner-name{font-size:19px;font-weight:500;color:var(--purple)}
.events-photo{left:20px;top:95px;width:220px;height:120px;background:linear-gradient(180deg,#c99b3b,#e8c36a 35%,#b88a38 60%,#3d3436)}

.footer{left:0;top:1099px;width:1064px;height:101px;background:var(--footer)}
.footer-nav{left:114px;top:1126px;font-size:13px;color:var(--purple)}
.footer-nav span.sep,.footer-legal span.sep{margin:0 9px}
.footer-legal{left:117px;top:1159px;font-size:13px;color:var(--purple)}
.social{left:822px;top:1146px;display:flex;gap:5px}
.social span{width:28px;height:28px;border-radius:50%;display:block}
</style>
</head>
<body>

<div class="abs top-bar"></div>
<div class="abs search">
  <div class="search-field">SEARCH</div>
  <div class="search-btn">
    <svg width="10" height="10" viewBox="0 0 10 10"><circle cx="4" cy="4" r="2.6" fill="none" stroke="#fff" stroke-width="1.4"/><line x1="6" y1="6" x2="8.6" y2="8.6" stroke="#fff" stroke-width="1.5"/></svg>
  </div>
</div>

<div class="abs brand">
  <span class="brand-dot"></span>
  <span class="brand-name">ORB Gala Hireworks</span>
</div>

<nav class="abs main-nav">
  <a href="#">Home</a><a href="#">Event Planning</a><a href="#">Catering</a><a href="#">Galleries</a><a href="#">Venues</a><a href="#">Contact Us</a>
</nav>

<div class="abs hero" role="img" aria-label="Banquet hall dressed with purple uplighting, draped columns, tables and a tiered cake"></div>

<form class="abs order-panel">
  <div class="order-title">Rental Orders Online</div>
  <div class="order-field">Name</div>
  <div class="order-field">E-Mail</div>
  <div class="order-field">Organisation/Company</div>
  <div class="order-field">Phone Number</div>
  <div class="order-field select">Budget</div>
  <span class="order-btn">Get An Order</span>
</form>

<svg class="abs slide-arrow slide-prev" viewBox="0 0 25 25"><circle cx="12.5" cy="12.5" r="12.5" fill="#eee"/><polyline points="14.5,7.5 9.5,12.5 14.5,17.5" fill="none" stroke="#333" stroke-width="2.4"/></svg>
<svg class="abs slide-arrow slide-next" viewBox="0 0 25 25"><circle cx="12.5" cy="12.5" r="12.5" fill="#f2692a"/><polyline points="10.5,7.5 15.5,12.5 10.5,17.5" fill="none" stroke="#333" stroke-width="2.4"/></svg>

<h1 class="abs welcome-title" style="font-weight:400">Welcome To ORB Gala Hireworks</h1>
<p class="abs welcome-text">Sed ut perspiciatis unde omnis iste natus error sit voluptatem accusantium doloremque laudantium, totam rem aperiam, eaque ipsa quae ab illo inventore veritatis et quasi architecto beatae vitae dicta sunt explicabo. Nemo enim ipsam voluptatem quia voluptas sit aspernatur aut odit aut fugit, sed quia consequuntur magni dolores eos qui ratione voluptatem sequi nesciunt.</p>

<section class="abs card card-how">
  <h2 class="card-title" style="font-weight:400">How it works</h2>
  <div class="abs video" role="img" aria-label="Video still of bridesmaids in lilac dresses holding bouquets">
    <span class="play"></span>
    <svg class="abs" style="left:108px;top:49px" width="10" height="10" viewBox="0 0 10 10"><polygon points="1,0 9,5 1,10" fill="#fff"/></svg>
    <div class="video-bar">
      <svg width="226" height="28" viewBox="0 0 226 28">
        <rect x="12" y="10" width="2.5" height="8" fill="#fff"/><rect x="16.5" y="10" width="2.5" height="8" fill="#fff"/>
        <rect x="47" y="12.5" width="172" height="3" rx="1.5" fill="#000"/>
        <rect x="47" y="12.5" width="55" height="3" rx="1.5" fill="#555"/>
        <circle cx="88" cy="14" r="2.6" fill="#fff"/>
        <polygon points="208,11 211,11 214,8 214,20 211,17 208,17" fill="#fff"/>
      </svg>
    </div>
  </div>
  <p class="card-copy" style="left:20px;top:211px;width:227px">Lorem Ipsum is simply dummy text of the printing and typesetting industry. Lorem Ipsum has been the industry's standard dummy text ever since the 1500s, when an unknown printer took a galley of type and scrambled</p>
</section>

<section class="abs card card-gallery">
  <h2 class="card-title" style="font-weight:400;left:22px">Photo Gallery</h2>
  <div class="abs gallery-main" role="img" aria-label="Evening reception guests beneath purple-lit trees">
    <svg class="g-arrow" style="left:9px" viewBox="0 0 24 24"><circle cx="12" cy="12" r="12" fill="#f2f2f2"/><polyline points="14,7 9,12 14,17" fill="none" stroke="#333" stroke-width="2.2"/></svg>
    <svg class="g-arrow" style="right:9px" viewBox="0 0 24 24"><circle cx="12" cy="12" r="12" fill="#f2f2f2"/><polyline points="10,7 15,12 10,17" fill="none" stroke="#333" stroke-width="2.2"/></svg>
  </div>
  <div class="abs thumb" style="left:20px;top:220px;background:linear-gradient(135deg,#2c3a8c,#8a6fd1)" role="img" aria-label="Stage with blue and violet lights"></div>
  <div class="abs thumb" style="left:97px;top:220px;background:linear-gradient(135deg,#a8364f,#e0a0b8)" role="img" aria-label="Pink-lit dining room"></div>
  <div class="abs thumb" style="left:174px;top:220px;background:linear-gradient(180deg,#5d8ec9,#e9eef2 60%,#5b7a3a)" role="img" aria-label="White marquee tent on a lawn"></div>
  <div class="abs thumb" style="left:20px;top:283px;background:linear-gradient(135deg,#3a2414,#c08a3e)" role="img" aria-label="Candle-lit banquet tables"></div>
  <div class="abs thumb" style="left:97px;top:283px;background:linear-gradient(135deg,#5a1f5e,#d64aa0)" role="img" aria-label="Magenta-lit dance floor"></div>
  <div class="abs thumb" style="left:174px;top:283px;background:linear-gradient(135deg,#9c968a,#e4e0d6)" role="img" aria-label="Tent interior with set tables"></div>
</section>

<section class="abs card card-events">
  <div class="abs partner">
    <span class="partner-dot"></span>
    <span class="partner-name">Bramblewick Affairs</span>
  </div>
  <h2 class="card-title" style="font-weight:400;left:22px;top:74px">Event Management</h2>
  <div class="abs events-photo" role="img" aria-label="Gilded ballroom filled with seated guests"></div>
  <p class="card-copy" style="left:23px;top:226px;width:244px">Lorem ipsum dolor sit amet, consectetur adipisicing elit, sed do eiusmod tempor incididunt ut labore et dolore magna aliqua. Ut enim ad minim veniam, quis nostrud exercitation ullamco laboris</p>
</section>

<footer class="abs footer"></footer>
<div class="abs footer-nav">Home<span class="sep">|</span>Event Planning<span class="sep">|</span>Catering<span class="sep">|</span>Galleries<span class="sep">|</span>Venues<span class="sep">|</span>Contact Us</div>
<div class="abs footer-legal">©2013 Company Name , All Rights Reserved<span class="sep">|</span>Privacy Policy<span class="sep">|</span>Terms &amp; Conditions</div>
<div class="abs social" aria-label="Social links">
  <span style="background:#3b5998"></span>
  <span style="background:#f58a1f"></span>
  <span style="background:#2aa3e0"></span>
  <span style="background:#e52d27"></span>
</div>

</body>
</html>
```